Real estate agent website

I am a new real estate agent and in of a simple but powerful website that is linked to the local Multiple listing services (MLS). It should have a lending page that is connected to my customer relationship management (CRM) software. It must have an ability for potential customers to search for properties and be able to communicate with me easily.
Updates

Updates: The website themes must includes MLS-IDX integration with a grid layout and property slider so i can showcase featured properties. I also would like to have future where potential client can search and have alerts depending on a search criteria.

Industry/Entity Type

Real Estate

Coding

Coded - Design and coding required

Number of Pages Required

3 page

Requirements
Must have
• Home page, Resources page, About Me with contact me window page

```html
<!DOCTYPE html>
<html lang="en">
<head>
<meta charset="utf-8">
<title>Marina Holt – Real Estate</title>
<link href="https://fonts.googleapis.com/css2?family=Montserrat:wght@400;500;600;700&display=swap" rel="stylesheet">
<style>
:root{
  --orange:#ef9b40;
  --ink:#2f2f33;
  --text:#4a4a4f;
  --muted:#6b6b70;
  --line:#e4e4e6;
  --about-bg:#efeff1;
  --touch-bg:#fcf8f3;
  --contact-bg:#fbf2e8;
  --footer:#6d6a79;
  --white:#fff;
}
*{box-sizing:border-box;margin:0;padding:0}
html,body{width:1200px;height:2951px;overflow:hidden}
body{font-family:'Montserrat',sans-serif;color:var(--text);background:var(--white);position:relative}
.btn{background:var(--orange);color:var(--white);border:none;font-family:inherit;font-weight:500;display:inline-flex;align-items:center;justify-content:center}

.site-header{position:absolute;top:0;left:0;width:1200px;height:79px;display:flex;align-items:center;padding:0 111px}
.brand{display:flex;align-items:center;gap:12px;font-size:28px;font-weight:500;color:var(--ink)}
.brand-mark{width:22px;height:22px;background:var(--orange)}
.main-nav{margin-left:auto;display:flex;gap:25px;align-items:center;font-size:16px;color:var(--text)}
.main-nav .active{color:var(--orange)}
.main-nav .btn{margin-left:6px;width:137px;height:39px;font-size:17px}

.hero{position:absolute;top:79px;left:0;width:1200px;height:473px;background:linear-gradient(180deg,#6f9bc9 0%,#a7c2dc 30%,#9a6a52 55%,#6b7a48 80%,#4f5e2e 100%)}
.hero-title{position:absolute;top:170px;width:100%;text-align:center;color:var(--white);line-height:1}
.hero-title .small{font-size:50px;font-weight:400;display:block}
.hero-title .big{font-size:60px;font-weight:700;display:block;margin-top:8px}
.search-bar{position:absolute;left:319px;top:338px;width:562px;height:75px;background:rgba(110,110,120,.55);display:flex;align-items:center;gap:14px;padding:0 16px}
.select{width:200px;height:42px;background:var(--white);font-size:15px;color:var(--text);display:flex;align-items:center;justify-content:space-between;padding:0 14px}
.search-bar .btn{width:97px;height:42px;font-size:16px}

.featured-title{position:absolute;top:598px;width:100%;text-align:center;font-size:42px;font-weight:400;color:#55545a;letter-spacing:1px}
.featured-title span,.sec-title span{color:var(--orange)}
.listings{position:absolute;top:684px;left:113px;display:grid;grid-template-columns:repeat(3,295px);column-gap:45px;row-gap:40px}
.card{height:449px;background:var(--white);box-shadow:0 2px 8px rgba(0,0,0,.16);padding:23px 22px 0}
.card-photo{height:183px;position:relative;background:linear-gradient(180deg,#9fc0e2,#c9c3b6 60%,#e9ecef)}
.card-photo.b{background:linear-gradient(180deg,#5e93d4,#b9735c 55%,#6e8a3e)}
.card-photo.c{background:linear-gradient(180deg,#c9d3dc,#7d7a73 55%,#f0f2f4)}
.card-photo.d{background:linear-gradient(180deg,#6f9bd6,#b8ab8c 55%,#8a8a78)}
.card-photo .heart{position:absolute;top:14px;right:13px}
.card h3{font-size:16px;font-weight:400;color:var(--ink);margin-top:28px}
.card .city{font-size:14px;margin-top:8px}
.specs{display:flex;align-items:center;gap:8px;font-size:14px;border-top:1px solid var(--line);border-bottom:1px solid var(--line);margin-top:12px;height:48px}
.specs .spec{display:flex;align-items:center;gap:7px;margin-right:16px}
.specs b{font-weight:500;color:var(--ink)}
.price-row{display:flex;justify-content:space-between;align-items:center;height:47px;border-bottom:1px solid var(--line);color:var(--orange);font-size:16px}
.mls{display:flex;align-items:center;gap:14px;height:58px;font-size:8.5px;line-height:1.5;white-space:nowrap}
.badge{width:82px;height:16px;background:#3a3a3e;border-radius:2px;flex:none}

.view-all{position:absolute;top:1665px;left:546px;width:108px;height:41px;font-size:16px}

.about{position:absolute;top:1765px;left:0;width:1200px;height:534px;background:var(--about-bg)}
.sec-title{font-size:42px;font-weight:400;color:#55545a;letter-spacing:1px}
.about .sec-title{position:absolute;top:84px;left:109px}
.about-text{position:absolute;top:157px;left:111px;width:545px;font-size:16px;line-height:30px;text-align:justify;color:var(--text)}
.about-text p+p{margin-top:7px}
.about-text .tagline{color:var(--ink);margin-top:0}
.photo-yard{position:absolute;top:62px;left:804px;width:286px;height:416px;background:linear-gradient(180deg,#8aa0b8,#6f8a4a 45%,#7a6f5f 75%,#a59074);box-shadow:0 2px 8px rgba(0,0,0,.2)}
.photo-portrait{position:absolute;top:97px;left:712px;width:173px;height:173px;background:linear-gradient(160deg,#e6e2dc,#cfa27e 55%,#f3efe9);box-shadow:0 2px 8px rgba(0,0,0,.2)}

.touch{position:absolute;top:2299px;left:0;width:601px;height:507px;background:var(--touch-bg)}
.contact{position:absolute;top:2299px;left:601px;width:599px;height:507px;background:var(--contact-bg)}
.touch .sec-title{position:absolute;top:80px;left:111px}
.form{position:absolute;top:152px;left:113px;width:401px}
.field{background:var(--white);height:53px;margin-bottom:9px;font-size:14px;padding:20px 18px;color:var(--text);border-radius:3px}
.field.msg{height:72px}
.form .btn{width:113px;height:41px;font-size:16px;font-weight:600;margin-top:12px}
.contact .sec-title{position:absolute;top:80px;left:68px}
.contact-item{position:absolute;left:68px;display:flex;gap:22px;font-size:17px;line-height:31px;color:var(--text)}
.contact-item svg{flex:none;margin-top:6px}

.site-footer{position:absolute;top:2806px;left:0;width:1200px;height:145px;background:var(--footer);color:var(--white);text-align:center}
.footer-nav{display:flex;justify-content:center;gap:31px;font-size:18px;margin-top:40px}
.copy{font-size:17px;margin-top:23px}
</style>
</head>
<body>

<header class="site-header">
  <div class="brand"><span class="brand-mark"></span>Marina Holt</div>
  <nav class="main-nav">
    <span class="active">Home</span><span>About</span><span>Listing</span><span>Lending</span><span>Contact</span>
    <span class="btn">Get a Quote</span>
  </nav>
</header>

<section class="hero" role="img" aria-label="Brick family house with garage under a blue sky">
  <h1 class="hero-title"><span class="small">Welcome to</span><span class="big">MARINA HOLT</span></h1>
  <div class="search-bar">
    <div class="select">City <svg width="10" height="6"><path d="M0 0h10L5 6z" fill="#333"/></svg></div>
    <div class="select">Zipcode <svg width="10" height="6"><path d="M0 0h10L5 6z" fill="#333"/></svg></div>
    <span class="btn">Search</span>
  </div>
</section>

<h2 class="featured-title"><span>FEATURED</span> LISTINGS</h2>

<div class="listings">
  <article class="card"><div class="card-photo" role="img" aria-label="Townhouse with snowy yard"><svg class="heart" width="20" height="18" viewBox="0 0 20 18"><path d="M10 18 1.5 9.5A5 5 0 0 1 10 3a5 5 0 0 1 8.5 6.5z" fill="#fff"/></svg></div><h3>20523 Birchwood Avenue</h3><p class="city">Lakeville, MN 55044</p><div class="specs"><span class="spec"><svg width="22" height="16" viewBox="0 0 22 16" fill="none" stroke="#333" stroke-width="1.5"><rect x="1" y="6" width="20" height="7"/><rect x="3" y="1" width="16" height="5"/><path d="M1 13v3M21 13v3"/></svg>3</span><span class="spec"><svg width="20" height="16" viewBox="0 0 20 16" fill="none" stroke="#333" stroke-width="1.5"><path d="M1 8h18v3a4 4 0 0 1-4 4H5a4 4 0 0 1-4-4zM4 8V2h4v2"/></svg>4</span><span class="spec"><b>Sq ft</b> 2,361</span></div><div class="price-row">$330,000<svg width="24" height="12" viewBox="0 0 24 12" fill="none" stroke="#ef9b40" stroke-width="2"><path d="M0 6h22M17 1l5 5-5 5"/></svg></div><div class="mls"><span class="badge"></span><span>MLS# NST1048275<br>Listing Office: Ashby Group LLC</span></div></article>
  <article class="card"><div class="card-photo b" role="img" aria-label="Red brick house with garden"><svg class="heart" width="20" height="18" viewBox="0 0 20 18"><path d="M10 18 1.5 9.5A5 5 0 0 1 10 3a5 5 0 0 1 8.5 6.5z" fill="#fff"/></svg></div><h3>20523 Birchwood Avenue</h3><p class="city">Lakeville, MN 55044</p><div class="specs"><span class="spec"><svg width="22" height="16" viewBox="0 0 22 16" fill="none" stroke="#333" stroke-width="1.5"><rect x="1" y="6" width="20" height="7"/><rect x="3" y="1" width="16" height="5"/><path d="M1 13v3M21 13v3"/></svg>3</span><span class="spec"><svg width="20" height="16" viewBox="0 0 20 16" fill="none" stroke="#333" stroke-width="1.5"><path d="M1 8h18v3a4 4 0 0 1-4 4H5a4 4 0 0 1-4-4zM4 8V2h4v2"/></svg>4</span><span class="spec"><b>Sq ft</b> 2,361</span></div><div class="price-row">$330,000<svg width="24" height="12" viewBox="0 0 24 12" fill="none" stroke="#ef9b40" stroke-width="2"><path d="M0 6h22M17 1l5 5-5 5"/></svg></div><div class="mls"><span class="badge"></span><span>MLS# NST1048275<br>Listing Office: Ashby Group LLC</span></div></article>
  <article class="card"><div class="card-photo c" role="img" aria-label="Two-storey house in winter"><svg class="heart" width="20" height="18" viewBox="0 0 20 18"><path d="M10 18 1.5 9.5A5 5 0 0 1 10 3a5 5 0 0 1 8.5 6.5z" fill="#fff"/></svg></div><h3>20523 Birchwood Avenue</h3><p class="city">Lakeville, MN 55044</p><div class="specs"><span class="spec"><svg width="22" height="16" viewBox="0 0 22 16" fill="none" stroke="#333" stroke-width="1.5"><rect x="1" y="6" width="20" height="7"/><rect x="3" y="1" width="16" height="5"/><path d="M1 13v3M21 13v3"/></svg>3</span><span class="spec"><svg width="20" height="16" viewBox="0 0 20 16" fill="none" stroke="#333" stroke-width="1.5"><path d="M1 8h18v3a4 4 0 0 1-4 4H5a4 4 0 0 1-4-4zM4 8V2h4v2"/></svg>4</span><span class="spec"><b>Sq ft</b> 2,361</span></div><div class="price-row">$330,000<svg width="24" height="12" viewBox="0 0 24 12" fill="none" stroke="#ef9b40" stroke-width="2"><path d="M0 6h22M17 1l5 5-5 5"/></svg></div><div class="mls"><span class="badge"></span><span>MLS# NST1048275<br>Listing Office: Ashby Group LLC</span></div></article>
  <article class="card"><div class="card-photo c" role="img" aria-label="House with garage and snow"><svg class="heart" width="20" height="18" viewBox="0 0 20 18"><path d="M10 18 1.5 9.5A5 5 0 0 1 10 3a5 5 0 0 1 8.5 6.5z" fill="#fff"/></svg></div><h3>20523 Birchwood Avenue</h3><p class="city">Lakeville, MN 55044</p><div class="specs"><span class="spec"><svg width="22" height="16" viewBox="0 0 22 16" fill="none" stroke="#333" stroke-width="1.5"><rect x="1" y="6" width="20" height="7"/><rect x="3" y="1" width="16" height="5"/><path d="M1 13v3M21 13v3"/></svg>3</span><span class="spec"><svg width="20" height="16" viewBox="0 0 20 16" fill="none" stroke="#333" stroke-width="1.5"><path d="M1 8h18v3a4 4 0 0 1-4 4H5a4 4 0 0 1-4-4zM4 8V2h4v2"/></svg>4</span><span class="spec"><b>Sq ft</b> 2,361</span></div><div class="price-row">$330,000<svg width="24" height="12" viewBox="0 0 24 12" fill="none" stroke="#ef9b40" stroke-width="2"><path d="M0 6h22M17 1l5 5-5 5"/></svg></div><div class="mls"><span class="badge"></span><span>MLS# NST1048275<br>Listing Office: Ashby Group LLC</span></div></article>
  <article class="card"><div class="card-photo d" role="img" aria-label="Split-level house with lawn"><svg class="heart" width="20" height="18" viewBox="0 0 20 18"><path d="M10 18 1.5 9.5A5 5 0 0 1 10 3a5 5 0 0 1 8.5 6.5z" fill="#fff"/></svg></div><h3>20523 Birchwood Avenue</h3><p class="city">Lakeville, MN 55044</p><div class="specs"><span class="spec"><svg width="22" height="16" viewBox="0 0 22 16" fill="none" stroke="#333" stroke-width="1.5"><rect x="1" y="6" width="20" height="7"/><rect x="3" y="1" width="16" height="5"/><path d="M1 13v3M21 13v3"/></svg>3</span><span class="spec"><svg width="20" height="16" viewBox="0 0 20 16" fill="none" stroke="#333" stroke-width="1.5"><path d="M1 8h18v3a4 4 0 0 1-4 4H5a4 4 0 0 1-4-4zM4 8V2h4v2"/></svg>4</span><span class="spec"><b>Sq ft</b> 2,361</span></div><div class="price-row">$330,000<svg width="24" height="12" viewBox="0 0 24 12" fill="none" stroke="#ef9b40" stroke-width="2"><path d="M0 6h22M17 1l5 5-5 5"/></svg></div><div class="mls"><span class="badge"></span><span>MLS# NST1048275<br>Listing Office: Ashby Group LLC</span></div></article>
  <article class="card"><div class="card-photo" role="img" aria-label="Large house in a snowy field"><svg class="heart" width="20" height="18" viewBox="0 0 20 18"><path d="M10 18 1.5 9.5A5 5 0 0 1 10 3a5 5 0 0 1 8.5 6.5z" fill="#fff"/></svg></div><h3>20523 Birchwood Avenue</h3><p class="city">Lakeville, MN 55044</p><div class="specs"><span class="spec"><svg width="22" height="16" viewBox="0 0 22 16" fill="none" stroke="#333" stroke-width="1.5"><rect x="1" y="6" width="20" height="7"/><rect x="3" y="1" width="16" height="5"/><path d="M1 13v3M21 13v3"/></svg>3</span><span class="spec"><svg width="20" height="16" viewBox="0 0 20 16" fill="none" stroke="#333" stroke-width="1.5"><path d="M1 8h18v3a4 4 0 0 1-4 4H5a4 4 0 0 1-4-4zM4 8V2h4v2"/></svg>4</span><span class="spec"><b>Sq ft</b> 2,361</span></div><div class="price-row">$330,000<svg width="24" height="12" viewBox="0 0 24 12" fill="none" stroke="#ef9b40" stroke-width="2"><path d="M0 6h22M17 1l5 5-5 5"/></svg></div><div class="mls"><span class="badge"></span><span>MLS# NST1048275<br>Listing Office: Ashby Group LLC</span></div></article>
</div>

<span class="btn view-all">View All</span>

<section class="about">
  <h2 class="sec-title"><span>ABOUT</span> ME</h2>
  <div class="about-text">
    <p>Purchasing or selling a house is the biggest investment venture that most of us will have in our lifetime. A home is a place of comfort and love. It is where we create memories. A place to live with our families and pets and enjoy our friends, and it’s a place where we create life-long memories.</p>
    <p>No matter what your goal or needs are in real estate, I would be honored to guide you through this journey. This is never just a business transaction; it will be a time where we would learn how to build trust that will sail our “ship” of relations throughout the years.</p>
    <p class="tagline">One happy client at a time!</p>
  </div>
  <div class="photo-yard" role="img" aria-label="Small dog sitting beneath a large tree in a backyard"></div>
  <div class="photo-portrait" role="img" aria-label="Portrait of the agent"></div>
</section>

<section class="touch">
  <h2 class="sec-title"><span>GET IN</span> TOUCH</h2>
  <div class="form">
    <div class="field">Name</div>
    <div class="field">Email</div>
    <div class="field msg">Message</div>
    <span class="btn">Submit</span>
  </div>
</section>

<section class="contact">
  <h2 class="sec-title"><span>CONTACT</span> US</h2>
  <div class="contact-item" style="top:161px"><svg width="20" height="26" viewBox="0 0 20 26"><path d="M10 0a10 10 0 0 1 10 10c0 7-10 16-10 16S0 17 0 10A10 10 0 0 1 10 0z" fill="#ef9b40"/><circle cx="10" cy="10" r="4" fill="#fbf2e8"/></svg><span>Northfield Home Group, Inc<br>4120 Cedar Ln Ste 310, Maple Grove,<br>Mn, 55311</span></div>
  <div class="contact-item" style="top:286px"><svg width="22" height="22" viewBox="0 0 24 24"><path d="M6.6 10.8a15 15 0 0 0 6.6 6.6l2.2-2.2a1 1 0 0 1 1-.25 11.4 11.4 0 0 0 3.6.6 1 1 0 0 1 1 1V20a1 1 0 0 1-1 1A17 17 0 0 1 3 4a1 1 0 0 1 1-1h3.5a1 1 0 0 1 1 1c0 1.25.2 2.45.6 3.6a1 1 0 0 1-.25 1z" fill="#ef9b40"/></svg><span>(612) 555-0148</span></div>
  <div class="contact-item" style="top:355px"><svg width="22" height="16" viewBox="0 0 22 16"><rect width="22" height="16" rx="1" fill="#ef9b40"/><path d="M1 1l10 8 10-8" fill="none" stroke="#fbf2e8" stroke-width="1.6"/></svg><span>hello@northfieldhomes.example</span></div>
</section>

<footer class="site-footer">
  <nav class="footer-nav"><span>Home</span><span>About</span><span>Listing</span><span>Lending</span><span>Contact Us</span><span>Book</span></nav>
  <p class="copy">2023 Marina Holt. All Rights Reserved.</p>
</footer>

</body>
</html>
```